Powerpoint design for spirits and cosmetics packaging company

We need a powerpoint template that will be used for company presentations, projects, award ceremonies etc... We are packaging in the wine and spirits sector as well as in the cosmetics sector. Our job is to package our customers' bottles in gift boxes, to carry out labeling, quality control, etc. We are based in Cognac.
We work for the big names in luxury: QDRT, Vellane Ostrow, Trelumo, Syvanne etc...
The template should be neat with at least 10 different slides.
Cover page, summary page, product description page (several), page including a schedule, price presentation page.

Target Market(s)

premium spirits and cosmetics

Industry/Entity Type

Spiritueux et cosmétique

Font styles to use
Sans Serif

Requirements
Must have
• My project must have the logo attached, the possibility to add / modify photos afterwards. Must have about ten different slides

```html
<!DOCTYPE html>
<html lang="fr">
<head>
<meta charset="utf-8">
<title>Atelier du Cormier – Modèle de présentation</title>
<link href="https://fonts.googleapis.com/css2?family=Montserrat:wght@400;500;600;700&display=swap" rel="stylesheet">
<style>
:root{
  --canvas:#575757;
  --red:#e8373f;
  --orange:#f7972b;
  --mid:#f0663a;
  --ink:#1d1d1d;
  --grey:#f1f0ef;
  --grey-dark:#e2e2e2;
  --paper:#ffffff;
  --grad-h:linear-gradient(90deg,var(--red),var(--orange));
  --grad-v:linear-gradient(180deg,var(--red),var(--orange));
}
*{box-sizing:border-box;margin:0;padding:0}
html,body{width:819px;height:1200px;overflow:hidden}
body{background:var(--canvas);font-family:'Montserrat',sans-serif;color:var(--ink);position:relative}
.slide{position:absolute;width:704px;height:396px;transform:scale(.5);transform-origin:0 0;overflow:hidden;background:var(--paper);box-shadow:2px 3px 6px rgba(0,0,0,.35)}
.slide > *{position:absolute}
.col-left{left:43px}.col-right{left:420px}
.row-1{top:64px}.row-2{top:283px}.row-3{top:502px}.row-4{top:722px}.row-5{top:940px}

.photo{background:linear-gradient(135deg,#8a6a4c,#c9a37a 45%,#5b4636)}
.photo.cool{background:linear-gradient(160deg,#9fb3b8,#d9d2c4 50%,#7d6a58)}
.photo.warm{background:linear-gradient(135deg,#6d4a2f,#d8a66b 55%,#3e2e22)}
.photo-frame{border:5px solid var(--orange);background:#fff;padding:9px}
.photo-frame .photo{width:100%;height:100%}

.bar-v{background:var(--grad-v)}
.bar-orange{background:var(--orange)}
.vertical-title{writing-mode:vertical-rl;transform:rotate(180deg);color:#fff;font-weight:600;font-size:22px;letter-spacing:1px;display:flex;align-items:center;justify-content:flex-end;padding-bottom:10px}
.title-band{background:var(--grad-h);color:#fff;font-weight:600;font-size:23px;letter-spacing:.5px;display:flex;align-items:center;padding:0 34px}

.brand-mini{display:flex;align-items:center;gap:5px;font-size:8px;line-height:1;font-weight:600;color:var(--red);letter-spacing:.5px}
.brand-mini .mark{width:14px;height:14px;background:var(--red)}
.footer-brand{left:26px;top:344px}
.footer-line{left:120px;top:369px;width:527px;height:2px;background:var(--orange)}
.footer-square{left:645px;top:355px;width:17px;height:17px;background:var(--orange)}

/* cover */
.cover-brand{left:26px;top:98px;display:flex;gap:10px}
.cover-brand .mark{width:36px;height:36px;background:var(--red)}
.cover-brand .name{font-size:17px;line-height:17px;color:var(--red);letter-spacing:1.5px;font-weight:500}
.cover-brand .name b{font-weight:500}
.cover-brand .tag{font-size:9px;line-height:10px;color:var(--orange);letter-spacing:1px;margin-top:3px;font-weight:500}
.cover-band{left:0;top:172px;width:312px;height:111px;background:var(--grad-h);color:#fff;font-weight:600;font-size:27px;line-height:34px;padding:22px 0 0 29px;letter-spacing:.5px}

/* toc */
.toc{background:#000}
.toc-list{left:321px;top:74px;list-style:none;color:#fff;font-size:10px;font-weight:600}
.toc-list li{height:23px;display:flex}
.toc-list span{width:27px}
.toc .brand-mini{color:#fff}

/* jobs */
.jobs{left:45px;top:46px;list-style:none;width:370px}
.jobs li{height:36px;padding-left:16px;position:relative}
.jobs li::before{content:"";position:absolute;left:0;top:2px;width:8px;height:8px;background:var(--orange)}
.jobs h3{font-size:8.5px;color:var(--red);font-weight:700;line-height:11px}
.jobs p{font-size:6.4px;line-height:8.5px;font-weight:500}

/* history */
.event{width:90px;font-size:6px;line-height:7.4px;text-align:center;font-weight:500}
.event .txt{background:var(--grey);padding:9px 6px;height:93px;display:flex;align-items:center}
.event .year{height:25px;color:#fff;font-weight:700;font-size:13px;display:flex;align-items:center;justify-content:center}
.year.r{background:var(--red)}.year.o{background:var(--orange)}.year.m{background:var(--mid)}
.event.low .txt{height:85px}
.timeline-line{height:2px;background:#9a9a9a}
.tick{width:2px;background:#9a9a9a}
.dot{width:9px;height:9px;border-radius:50%;background:var(--orange)}

/* product */
.product-text{font-size:9px;line-height:11.4px;text-align:justify;font-weight:600}
.thumbs{display:flex;gap:2px}
.thumbs div{flex:1}

/* schedule */
.step .label{font-size:8px;font-weight:700;color:var(--red);position:absolute;top:0;left:0;white-space:nowrap}
.step .corner{position:absolute;left:0;top:12px;width:50px;height:42px;border-left:7px solid var(--red);border-top:7px solid var(--red);border-image:linear-gradient(135deg,var(--red),var(--orange)) 1}
.step p{position:absolute;left:20px;top:46px;font-size:7.4px;line-height:9.5px;font-weight:600;width:300px}

/* pricing */
.price-panel{left:24px;top:45px;width:586px;height:275px;background:var(--grey);border:1.5px solid var(--red)}
.pkg{top:87px;height:41px;color:#fff;font-size:13px;font-weight:500;display:flex;align-items:center;justify-content:center;letter-spacing:.5px}
.price-row{left:43px;width:548px;height:20.8px;font-size:10px;font-weight:500;padding-left:11px;display:flex;align-items:center}
.price-row:nth-of-type(odd){background:var(--grey-dark)}
.price-row:nth-of-type(even){background:#fff}

/* expertise */
.expert-panel{left:115px;top:46px;width:430px;height:277px;border:1.5px solid var(--red)}
.cell{background:#f5f5f5;width:124px;text-align:center;padding-top:12px}
.cell svg{width:30px;height:30px}
.cell h4{font-size:7.5px;font-weight:600;margin:4px 0 8px}
.cell p{font-size:5px;line-height:7px;color:#888;padding:0 10px}

/* contact */
.contact-brand{left:132px;top:33px}
.contact-brand .mark{position:absolute;left:-102px;top:0;width:60px;height:60px;background:var(--red)}
.contact-brand .name{font-size:24px;line-height:24px;color:var(--red);letter-spacing:2px;font-weight:500}
.contact-brand .tag{font-size:14px;line-height:16px;color:var(--orange);letter-spacing:1.5px;margin-top:4px}
.contact-rule{left:29px;top:180px;width:10px;height:216px;background:var(--red)}
.contact-item{left:60px;display:flex;gap:9px}
.contact-item svg{width:18px;height:18px;flex:none}
.contact-item h5{font-size:9.5px;color:var(--orange);font-weight:700;line-height:11px}
.contact-item p{font-size:10px;line-height:12.5px;font-weight:600}
</style>
</head>
<body>

<!-- 1 · cover -->
<section class="slide col-left row-1">
  <div class="cover-brand">
    <div class="mark"></div>
    <div>
      <div class="name">ATELIER<br><b>DU CORMIER</b></div>
      <div class="tag">CO-PACKING<br>SERVICES</div>
    </div>
  </div>
  <div class="cover-band">VINS, SPIRITUEUX<br>&amp; COSMÉTIQUES</div>
  <div class="photo-frame" style="left:312px;top:124px;width:239px;height:239px">
    <div class="photo" role="img" aria-label="Photo : mains tenant une bouteille de cognac sur la ligne de conditionnement"></div>
  </div>
</section>

<!-- 2 · table of content -->
<section class="slide toc col-right row-1">
  <div class="bar-v" style="left:27px;top:0;width:244px;height:33px;background:var(--red)"></div>
  <div class="bar-v vertical-title" style="left:27px;top:0;width:29px;height:332px;font-size:20px">TABLE OF CONTENT</div>
  <div class="photo cool" style="left:56px;top:33px;width:215px;height:299px" role="img" aria-label="Photo : bouteille de rhum sur un convoyeur en atelier"></div>
  <ol class="toc-list">
    <li><span>1</span>Nos emplois</li>
    <li><span>2</span>Notre histoire</li>
    <li><span>3</span>Expertises &amp; Savoir-Faire</li>
    <li><span>4</span>Product 1</li>
    <li><span>5</span>Product 2</li>
    <li><span>6</span>Product 3</li>
    <li><span>7</span>Product 4</li>
    <li><span>8</span>Schedule</li>
    <li><span>9</span>Pricing</li>
    <li><span>10</span>Contact</li>
  </ol>
  <div class="brand-mini footer-brand"><div class="mark"></div><div>ATELIER<br>DU CORMIER</div></div>
  <div class="footer-line" style="left:298px"></div>
  <div class="footer-square"></div>
</section>

<!-- 3 · nos emplois -->
<section class="slide col-left row-2">
  <div class="title-band" style="left:177px;top:0;width:285px;height:31px;justify-content:flex-end;padding-right:32px;background:linear-gradient(90deg,#fff,var(--red) 30%,var(--orange))">NOS EMPLOIS</div>
  <div class="bar-orange" style="left:430px;top:0;width:32px;height:322px"></div>
  <div class="photo cool" style="left:462px;top:0;width:242px;height:322px" role="img" aria-label="Photo : atelier de conditionnement avec palettes et lignes de production"></div>
  <ul class="jobs">
    <li><h3>DÉVELOPPEMENT PACKAGING</h3><p>Lorem ipsum dolor sit amet, consectetur adipiscing elit. Sed volutpat pretium pharetra.<br>Maecenas porta diam justo, vitae hendrerit nisi commodo et.</p></li>
    <li><h3>CONTRÔLE QUALITÉ</h3><p>Lorem ipsum dolor sit amet, consectetur adipiscing elit. Sed volutpat pretium pharetra.<br>Maecenas porta diam justo, vitae hendrerit nisi commodo et.</p></li>
    <li><h3>ÉDITIONS LIMITÉES</h3><p>Lorem ipsum dolor sit amet, consectetur adipiscing elit. Sed volutpat pretium pharetra.<br>Maecenas porta diam justo, vitae hendrerit nisi commodo et.</p></li>
    <li><h3>COFFRETS CADEAUX</h3><p>Lorem ipsum dolor sit amet, consectetur adipiscing elit. Sed volutpat pretium pharetra.<br>Maecenas porta diam justo, vitae hendrerit nisi commodo et.</p></li>
    <li><h3>POSE D'ACCESSOIRES</h3><p>Lorem ipsum dolor sit amet, consectetur adipiscing elit. Sed volutpat pretium pharetra.<br>Maecenas porta diam justo, vitae hendrerit nisi commodo et.</p></li>
    <li><h3>POSE DE BANDES FISCALES</h3><p>Lorem ipsum dolor sit amet, consectetur adipiscing elit. Sed volutpat pretium pharetra.<br>Maecenas porta diam justo, vitae hendrerit nisi commodo et.</p></li>
    <li><h3>MISE EN ÉTUI</h3><p>Lorem ipsum dolor sit amet, consectetur adipiscing elit. Sed volutpat pretium pharetra.<br>Maecenas porta diam justo, vitae hendrerit nisi commodo et.</p></li>
    <li><h3>REPIQUAGE DE COFFRETS</h3><p>Lorem ipsum dolor sit amet, consectetur adipiscing elit. Sed volutpat pretium pharetra.<br>Maecenas porta diam justo, vitae hendrerit nisi commodo et.</p></li>
  </ul>
  <div class="brand-mini footer-brand"><div class="mark"></div><div>ATELIER<br>DU CORMIER</div></div>
  <div class="footer-line"></div>
  <div class="footer-square"></div>
</section>

<!-- 4 · notre histoire -->
<section class="slide col-right row-2">
  <div class="bar-orange" style="left:0;top:0;width:56px;height:31px"></div>
  <div class="bar-orange vertical-title" style="left:26px;top:0;width:30px;height:288px">NOTRE HISTOIRE</div>

  <div class="event" style="left:118px;top:27px"><div class="txt">Ouverture d'un atelier dédié au montage des coffrets et étuis en carton.</div><div class="year r">2000</div></div>
  <div class="event" style="left:217px;top:27px"><div class="txt">Ouverture d'un atelier dédié au montage des coffrets et étuis en carton.</div><div class="year r">2008</div></div>
  <div class="event" style="left:314px;top:27px"><div class="txt">Ouverture d'un atelier dédié au montage des coffrets et étuis en carton.</div><div class="year m">2012</div></div>
  <div class="event" style="left:412px;top:27px"><div class="txt">Ouverture d'un atelier dédié au montage des coffrets et étuis en carton.</div><div class="year o">2015</div></div>
  <div class="event" style="left:510px;top:27px"><div class="txt">Ouverture d'un atelier dédié au montage des coffrets et étuis en carton.</div><div class="year o">2018</div></div>

  <div class="timeline-line" style="left:116px;top:181px;width:489px"></div>
  <div class="tick" style="left:162px;top:160px;height:22px"></div><div class="dot" style="left:158px;top:156px"></div>
  <div class="tick" style="left:261px;top:160px;height:22px"></div><div class="dot" style="left:257px;top:156px"></div>
  <div class="tick" style="left:358px;top:160px;height:22px"></div><div class="dot" style="left:354px;top:156px"></div>
  <div class="tick" style="left:456px;top:160px;height:22px"></div><div class="dot" style="left:452px;top:156px"></div>
  <div class="tick" style="left:554px;top:160px;height:22px"></div><div class="dot" style="left:550px;top:156px"></div>

  <div class="tick" style="left:114px;top:181px;height:20px"></div><div class="dot" style="left:110px;top:198px"></div>
  <div class="tick" style="left:212px;top:181px;height:20px"></div><div class="dot" style="left:208px;top:198px"></div>
  <div class="tick" style="left:311px;top:181px;height:20px"></div><div class="dot" style="left:307px;top:198px"></div>
  <div class="tick" style="left:409px;top:181px;height:20px"></div><div class="dot" style="left:405px;top:198px"></div>
  <div class="tick" style="left:506px;top:181px;height:20px"></div><div class="dot" style="left:502px;top:198px"></div>
  <div class="tick" style="left:604px;top:181px;height:20px"></div><div class="dot" style="left:600px;top:198px"></div>

  <div class="event low" style="left:70px;top:214px"><div class="year r">1995</div><div class="txt">Ouverture d'un atelier dédié au montage des coffrets et étuis en carton.</div></div>
  <div class="event low" style="left:167px;top:214px"><div class="year r">2007</div><div class="txt">Ouverture d'un atelier dédié au montage des coffrets et étuis en carton.</div></div>
  <div class="event low" style="left:266px;top:214px"><div class="year m">2010</div><div class="txt">Ouverture d'un atelier dédié au montage des coffrets et étuis en carton.</div></div>
  <div class="event low" style="left:364px;top:214px"><div class="year m">2014</div><div class="txt">Ouverture d'un atelier dédié au montage des coffrets et étuis en carton.</div></div>
  <div class="event low" style="left:461px;top:214px"><div class="year o">2017</div><div class="txt">Ouverture d'un atelier dédié au montage des coffrets et étuis en carton.</div></div>
  <div class="event low" style="left:559px;top:214px"><div class="year o">2020</div><div class="txt">Ouverture d'un atelier dédié au montage des coffrets et étuis en carton.</div></div>

  <div class="brand-mini footer-brand"><div class="mark"></div><div>ATELIER<br>DU CORMIER</div></div>
  <div class="footer-line"></div>
  <div class="footer-square"></div>
</section>

<!-- 5 · product 1 -->
<section class="slide col-left row-3">
  <div class="title-band" style="left:27px;top:0;width:243px;height:32px;background:linear-gradient(90deg,var(--red),#ec4a3c)">PRODUCT 1</div>
  <div class="bar-v" style="left:27px;top:0;width:33px;height:334px"></div>
  <p class="product-text" style="left:87px;top:104px;width:277px">Lorem ipsum dolor sit amet, consectetur adipiscing elit. Sed volutpat pretium pharetra. Maecenas porta diam justo, vitae hendrerit nisi commodo et. Quisque eu metus condimentum, suscipit augue nec, hendrerit enim. Fusce vitae fringilla nisi, ultrices congue urna. In porttitor lacinia mi at accumsan. Donec pharetra mi a sem cursus congue. Curabitur suscipit consectetur dolor, sed rhoncus diam porta vel. Sed consequat egestas bibendum. Proin nec ex est.</p>
  <div class="thumbs" style="left:87px;top:226px;width:277px;height:61px">
    <div class="photo warm" role="img" aria-label="Photo : bouteille de cognac en cours d'habillage"></div>
    <div class="photo" role="img" aria-label="Photo : pose d'une étiquette sur une carafe"></div>
    <div class="photo warm" role="img" aria-label="Photo : mise en coffret d'une bouteille"></div>
  </div>
  <div class="photo-frame" style="left:398px;top:102px;width:182px;height:185px;padding:8px">
    <div class="photo warm" role="img" aria-label="Photo : mains ajustant le bouchon d'une carafe de cognac XO"></div>
  </div>
  <div class="brand-mini footer-brand"><div class="mark"></div></div>
  <div class="footer-line"></div>
  <div class="footer-square"></div>
</section>

<!-- 6 · product 2 -->
<section class="slide col-right row-3">
  <div class="title-band" style="left:27px;top:0;width:243px;height:32px;background:linear-gradient(90deg,var(--red),#ec4a3c)">PRODUCT 2</div>
  <div class="bar-v" style="left:27px;top:0;width:33px;height:334px"></div>
  <p class="product-text" style="left:85px;top:104px;width:303px">Lorem ipsum dolor sit amet, consectetur adipiscing elit. Sed volutpat pretium pharetra. Maecenas porta diam justo, vitae hendrerit nisi commodo et. Quisque eu metus condimentum, suscipit augue nec, hendrerit enim. Fusce vitae fringilla nisi, ultrices congue urna. In porttitor lacinia mi at accumsan. Donec pharetra mi a sem cursus congue. Curabitur suscipit consectetur dolor, sed rhoncus diam porta vel. Sed consequat egestas bibendum. Proin nec ex est.</p>
  <div class="thumbs" style="left:85px;top:226px;width:303px;height:66px">
    <div class="photo cool" role="img" aria-label="Photo : ligne de conditionnement en atelier"></div>
    <div class="photo" role="img" aria-label="Photo : contrôle d'une bouteille à la main"></div>
    <div class="photo warm" role="img" aria-label="Photo : bouchage d'une bouteille de rhum"></div>
  </div>
  <div class="photo-frame" style="left:430px;top:102px;width:131px;height:185px;padding:7px">
    <div class="photo cool" role="img" aria-label="Photo : bouteille de rhum debout sur un convoyeur"></div>
  </div>
  <div class="brand-mini footer-brand"><div class="mark"></div></div>
  <div class="footer-line"></div>
  <div class="footer-square"></div>
</section>

<!-- 7 · schedule -->
<section class="slide col-left row-4">
  <div class="bar-orange" style="left:0;top:5px;width:30px;height:33px"></div>
  <div class="bar-orange vertical-title" style="left:27px;top:5px;width:30px;height:322px">SCHEDULE</div>

  <div class="step" style="left:490px;top:23px"><span class="label">AUG 2023</span><div class="corner"></div><p style="width:200px">Lorem ipsum dolor sit amet,<br>consectetur adipiscing elit.</p></div>
  <div class="step" style="left:414px;top:71px"><span class="label">JULY 2023</span><div class="corner"></div><p style="width:240px">Lorem ipsum dolor sit amet, consectetur adipiscing elit.<br>Sed volutpat pretium pharetra.</p></div>
  <div class="step" style="left:341px;top:118px"><span class="label">JUNE 2023</span><div class="corner"></div><p style="width:300px">Lorem ipsum dolor sit amet, consectetur adipiscing elit. Sed volutpat pretium pharetra. Maecenas porta diam justo, vitae hendrerit nisi</p></div>
  <div class="step" style="left:267px;top:168px"><span class="label">MAY 2023</span><div class="corner"></div><p style="width:360px">Lorem ipsum dolor sit amet, consectetur adipiscing elit. Sed volutpat pretium pharetra. Maecenas porta diam justo, vitae hendrerit nisi commodo et.</p></div>
  <div class="step" style="left:192px;top:216px"><span class="label">APRIL 2023</span><div class="corner"></div><p style="width:360px">Lorem ipsum dolor sit amet, consectetur adipiscing elit. Sed volutpat pretium pharetra. Maecenas porta diam justo, vitae hendrerit nisi commodo et.</p></div>
  <div class="step" style="left:117px;top:263px"><span class="label">MARCH 2023</span><div class="corner"></div><p style="width:360px">Lorem ipsum dolor sit amet, consectetur adipiscing elit. Sed volutpat pretium pharetra. Maecenas porta diam justo, vitae hendrerit nisi commodo et.</p></div>

  <div class="brand-mini footer-brand"><div class="mark"></div><div>ATELIER<br>DU CORMIER</div></div>
  <div class="footer-line"></div>
  <div class="footer-square"></div>
</section>

<!-- 8 · pricing -->
<section class="slide col-right row-4">
  <div class="price-panel"></div>
  <div class="title-band" style="left:399px;top:0;width:257px;height:31px;justify-content:flex-end;padding-right:26px">PRICING TABLE</div>
  <div class="bar-orange" style="left:626px;top:0;width:30px;height:320px"></div>
  <div class="pkg" style="left:219px;width:120px;background:var(--red)">PACKAGE 1</div>
  <div class="pkg" style="left:343px;width:122px;background:var(--mid)">PACKAGE 2</div>
  <div class="pkg" style="left:469px;width:120px;background:var(--orange)">PACKAGE 3</div>
  <div class="price-row" style="top:136px">Lorem Ipsum</div>
  <div class="price-row" style="top:157px">Lorem Ipsum</div>
  <div class="price-row" style="top:178px">Lorem Ipsum</div>
  <div class="price-row" style="top:199px">Lorem Ipsum</div>
  <div class="price-row" style="top:220px">Lorem Ipsum</div>
  <div class="price-row" style="top:241px">Lorem Ipsum</div>
  <div class="price-row" style="top:262px">Lorem Ipsum</div>
  <div class="brand-mini footer-brand"><div class="mark"></div><div>ATELIER<br>DU CORMIER</div></div>
  <div class="footer-line"></div>
  <div class="footer-square"></div>
</section>

<!-- 9 · expertises -->
<section class="slide col-left row-5">
  <div class="expert-panel"></div>
  <div class="title-band" style="left:115px;top:0;width:532px;height:33px;justify-content:center">EXPERTISES &amp; SAVOIR-FAIRE</div>
  <div class="bar-orange" style="left:615px;top:0;width:32px;height:335px"></div>

  <div class="cell" style="left:135px;top:58px;height:117px">
    <svg viewBox="0 0 30 30" fill="none" stroke="#e8373f" stroke-width="1.3"><path d="M9 5h12v7a6 6 0 0 1-12 0z"/><path d="M9 7H5a4 4 0 0 0 4 5M21 7h4a4 4 0 0 1-4 5M15 18v5M10 26h10M11 23h8"/></svg>
    <h4>Performance</h4><p>Notre savoir-faire technique au service de votre efficacité et de votre réactivité.</p>
  </div>
  <div class="cell" style="left:267px;top:58px;height:117px">
    <svg viewBox="0 0 30 30" fill="none" stroke="#e8373f" stroke-width="1.3"><path d="M15 4l2.5 5 5.5.8-4 3.9.9 5.5-4.9-2.6-4.9 2.6.9-5.5-4-3.9 5.5-.8z"/><path d="M6 26h18"/></svg>
    <h4>Qualité</h4><p>Une traçabilité complète et une démarche qualité suivie à chaque étape de production.</p>
  </div>
  <div class="cell" style="left:400px;top:58px;height:117px">
    <svg viewBox="0 0 30 30" fill="none" stroke="#e8373f" stroke-width="1.3"><circle cx="15" cy="13" r="8"/><path d="M11.5 13l2.5 2.5 4.5-5M10 20l-2 7 7-3 7 3-2-7"/></svg>
    <h4>Exception</h4><p>Des finitions soignées et des solutions manuelles adaptées à vos projets les plus exigeants.</p>
  </div>
  <div class="cell" style="left:135px;top:185px;height:130px">
    <svg viewBox="0 0 30 30" fill="none" stroke="#e8373f" stroke-width="1.3"><circle cx="15" cy="16" r="10"/><path d="M15 10v6l4 3M12 3h6M15 3v3"/></svg>
    <h4>Flexibilité</h4><p>Des équipes mobiles qui s'adaptent à vos volumes, dans nos ateliers ou sur site.</p>
  </div>
  <div class="cell" style="left:267px;top:185px;height:130px">
    <svg viewBox="0 0 30 30" fill="none" stroke="#e8373f" stroke-width="1.3"><path d="M4 16l6-6 5 4 5-4 6 6-6 6-5-4-5 4z"/><path d="M12 17l3 3 3-3"/></svg>
    <h4>Accompagnement</h4><p>Un suivi attentif de votre projet, du premier prototype jusqu'à la livraison finale.</p>
  </div>
  <div class="cell" style="left:400px;top:185px;height:130px">
    <svg viewBox="0 0 30 30" fill="none" stroke="#e8373f" stroke-width="1.3"><circle cx="15" cy="15" r="10"/><ellipse cx="15" cy="15" rx="4.5" ry="10"/><path d="M5 15h20M7 10h16M7 20h16"/></svg>
    <h4>Proximité</h4><p>Une flotte de véhicules et des entrepôts sécurisés pour stocker et livrer vos marchandises.</p>
  </div>

  <div class="brand-mini footer-brand"><div class="mark"></div><div>ATELIER<br>DU CORMIER</div></div>
  <div class="footer-line"></div>
  <div class="footer-square"></div>
</section>

<!-- 10 · contact -->
<section class="slide col-right row-5">
  <div class="photo" style="left:409px;top:0;width:295px;height:396px;background:linear-gradient(160deg,#e0503a,#ee7a3a 50%,#f39a3a)" role="img" aria-label="Photo : camion de livraison stationné devant l'entrepôt, teintée orange"></div>
  <div class="contact-brand">
    <div class="mark"></div>
    <div class="name">ATELIER<br>DU CORMIER</div>
    <div class="tag">CO-PACKING<br>SERVICES</div>
  </div>
  <div class="contact-rule"></div>
  <div class="contact-item" style="top:188px">
    <svg viewBox="0 0 20 20" fill="none" stroke="#e8373f" stroke-width="1.3"><path d="M10 18s6-6 6-10a6 6 0 0 0-12 0c0 4 6 10 6 10z"/><circle cx="10" cy="8" r="2.2"/></svg>
    <div><h5>Nous situer</h5><p>Parc des Ormeaux,<br>12 Rue des Chais,<br>16100 Cormanville</p></div>
  </div>
  <div class="contact-item" style="top:253px">
    <svg viewBox="0 0 20 20" fill="none" stroke="#e8373f" stroke-width="1.3"><path d="M5 3h3l1.5 4-2 1.5a9 9 0 0 0 4 4l1.5-2 4 1.5v3a2 2 0 0 1-2 2A14 14 0 0 1 3 5a2 2 0 0 1 2-2z"/></svg>
    <div><h5>Nous appeler</h5><p>05 40 12 78 30</p></div>
  </div>
  <div class="contact-item" style="top:291px">
    <svg viewBox="0 0 20 20" fill="none" stroke="#e8373f" stroke-width="1.3"><rect x="2.5" y="5" width="15" height="10"/><path d="M2.5 5l7.5 6 7.5-6"/></svg>
    <div><h5>Nous écrire</h5><p>contact@atelierducormier.fr</p></div>
  </div>
  <div class="contact-item" style="top:329px">
    <svg viewBox="0 0 20 20" fill="none" stroke="#e8373f" stroke-width="1.3"><rect x="2.5" y="6" width="15" height="10"/><path d="M7 6V4h6v2M2.5 10h15"/></svg>
    <div><h5>Nous consulter</h5><p>05 40 12 78 30</p></div>
  </div>
</section>

</body>
</html>
```